magcian / mentalist needs flyer desined to send potentisl clients

I need a design that's contemporary, sharp, fun, and professional that will get the attention of whoever receives the flyer very quickly. This is for a tri-fold flyer design.

I've been performing magic for over 40 years. I've performed close-up,
parlor, and stage shows. I've been an Master of Ceremonies, Key Note
Speaker (using magic during presentations to help build on a point or
topic, while keeping the audience entertained and educated on the topic or
topics the client has asked me to focus). I've worked trade shows and
sales training incorporating magic as well. I did private shows in Las
Vegas and L.A. back in the late 90's as well.

I do have website / tobiaskellwoodillusions.example for your to check out.

Target Market(s)

The target audience is corporation Event Planners, Marketing and Sales
managers, casino & hotel entertainment directors, as well as private
businesses looking for unique entertainment options.

Industry/Entity Type

Entertainment Industry

Logo Text

Here are a couple of ideas: your mind is my playground, neural entertainer, professor of mysteries, master of your mind

Requirements
Must have
• I like the black and white look (I think it looks nice, but open to other
• ideas and creativity. Being I'm a magician and mentalist, I'd like for
• both venues to be conveyed somehow. My magic is clean and corporate and family friendly.
Nice to have
• I do have website / tobiaskellwoodillusions.example for your to check out.
• My current business card is attached for review. I'll also attach photos
• I'd like to share, but was unable when I last attempted do sign up. Some
• of the files were too big and I'm not savvy enough to make them smaller,
• but think there might be some potential with a couple.
Should not have
• cartoons or cartoonish graphics. no rabbits, doves, magicians, wands, or top hats.

```html
<!DOCTYPE html>
<html lang="en">
<head>
<meta charset="utf-8">
<title>Tobias Kellwood – Tri-fold Brochure</title>
<link href="https://fonts.googleapis.com/css2?family=Jost:ital,wght@0,400;0,500;0,700;0,800;1,700;1,800&family=Josefin+Sans:wght@400;600;700&display=swap" rel="stylesheet">
<style>
:root{
  --ink:#0a0a0a;
  --paper:#ffffff;
  --stage:#e9e9e9;
  --mute:#bdbdbd;
  --photo-warm-a:#4a3526;
  --photo-warm-b:#1b120c;
  --photo-gray-a:#6f6f6f;
  --photo-gray-b:#1c1c1c;
  --photo-room-a:#b08a5a;
  --photo-room-b:#5a3d22;
}
*{box-sizing:border-box;margin:0;padding:0}
html,body{width:1200px;height:1200px;overflow:hidden;background:var(--stage)}
body{font-family:"Josefin Sans",sans-serif;color:var(--paper);position:relative}
.spread{position:absolute;left:40px;width:1120px;height:520px;display:flex;box-shadow:0 4px 18px rgba(0,0,0,.25)}
.spread--outside{top:40px}
.spread--inside{top:630px}
.panel{position:relative;width:373.33px;height:100%;overflow:hidden;background:var(--ink)}
.photo{position:absolute;display:block}
.photo--warm{background:linear-gradient(160deg,var(--photo-warm-a),var(--photo-warm-b))}
.photo--gray{background:linear-gradient(160deg,var(--photo-gray-a),var(--photo-gray-b))}
.photo--room{background:linear-gradient(160deg,var(--photo-room-a),var(--photo-room-b))}
.band{position:absolute;background:var(--paper)}

/* outside: services panel */
.services__photo{left:0;top:0;width:100%;height:160px}
.services__headline{position:absolute;left:22px;top:150px;right:22px;background:var(--ink);padding:8px 10px;font-family:"Jost",sans-serif;font-weight:800;font-style:italic;font-size:17px;line-height:1.22}
.service{position:absolute;left:28px;right:28px}
.service__tag{display:inline-block;background:var(--paper);color:var(--ink);font-family:"Jost",sans-serif;font-weight:700;font-style:italic;font-size:11px;padding:2px 7px;margin-bottom:3px}
.service__text{font-size:10px;line-height:1.35}

/* outside: intro panel */
.intro__ring{position:absolute;left:96px;top:30px;width:180px;height:180px;border-radius:50%;border:10px solid var(--mute);overflow:hidden}
.intro__ring .photo{inset:0}
.intro__text{position:absolute;left:50px;right:50px;top:240px;font-size:13px;line-height:1.35;text-align:center;font-style:italic}
.intro__cta{left:0;right:0;top:338px;height:30px;color:var(--ink);font-family:"Jost",sans-serif;font-weight:700;font-style:italic;font-size:12.5px;text-align:center;line-height:30px}
.contact{position:absolute;left:30px;top:390px;font-family:"Jost",sans-serif;font-weight:700;font-size:13px;line-height:24px}
.contact__row{display:flex;align-items:center;gap:8px;white-space:nowrap}
.contact__row svg{width:13px;height:13px;flex:none}

/* outside: cover */
.cover__strip{left:40px;right:20px;height:70px}
.cover__name{left:0;right:0;top:348px;height:44px;color:var(--ink);font-family:"Jost",sans-serif;font-weight:800;font-size:32px;letter-spacing:.3px;line-height:44px;text-align:right;padding-right:16px;white-space:nowrap}
.cover__tagline{position:absolute;right:18px;top:400px;font-family:"Jost",sans-serif;font-weight:700;font-size:17px}
.cover__phone{left:40px;top:445px;width:200px;height:40px;color:var(--ink);font-family:"Jost",sans-serif;font-weight:800;font-size:19px;line-height:40px;text-align:center}

/* inside: about */
.about{background:var(--paper);color:var(--ink)}
.about__title{position:absolute;left:28px;top:48px;font-family:"Jost",sans-serif;font-weight:800;font-size:18px;line-height:1.1}
.about__body{position:absolute;left:28px;right:30px;top:100px;font-size:11.5px;line-height:1.45}
.about__body p{margin-bottom:10px}
.about__body b{font-weight:700}

/* inside: services list */
.offer__photo{left:0;top:0;width:100%;height:330px}
.offer__tab{left:18px;top:10px;padding:4px 12px;color:var(--ink);font-family:"Jost",sans-serif;font-weight:800;font-size:17px}
.offer__list{position:absolute;left:0;right:0;top:118px;text-align:center;font-family:"Jost",sans-serif;font-weight:700;font-size:14px;line-height:18px;letter-spacing:.5px}
.offer__item{margin-bottom:14px}
.offer__icon{display:block;width:10px;height:10px;margin:0 auto 5px;background:var(--paper)}
.offer__room{left:0;top:330px;width:100%;height:190px}

/* inside: guarantee */
.promise{background:var(--paper);color:var(--ink)}
.promise__photo{left:0;top:0;width:100%;height:215px}
.promise__tag{position:absolute;left:14px;top:18px;background:var(--ink);color:var(--paper);font-family:"Jost",sans-serif;font-weight:800;font-size:11.5px;line-height:1.25;padding:4px 7px}
.promise__note{position:absolute;left:14px;right:120px;top:84px;background:rgba(0,0,0,.85);color:var(--paper);font-size:9.5px;line-height:1.35;padding:7px 9px}
.promise__name{position:absolute;right:0;top:0;width:96px;height:44px;background:var(--paper);color:var(--ink);font-family:"Jost",sans-serif;font-weight:800;font-size:11px;line-height:1.05;text-align:right;padding:10px 10px 0 0}
.promise__thumb{left:10px;width:135px;height:78px}
.promise__heads{position:absolute;left:165px;top:232px}
.promise__heads span{display:inline-block;background:var(--ink);color:var(--paper);font-family:"Jost",sans-serif;font-weight:800;font-size:12px;padding:2px 6px;margin-bottom:3px}
.promise__body{position:absolute;left:160px;right:14px;top:288px;font-size:9.8px;line-height:1.38}
.promise__footer{position:absolute;left:0;right:0;bottom:0;height:40px;background:var(--ink);color:var(--paper);font-family:"Jost",sans-serif;font-weight:500;font-size:12.5px;line-height:40px;text-align:right;padding-right:14px}
</style>
</head>
<body>

<section class="spread spread--outside">
  <div class="panel services">
    <div class="photo photo--warm services__photo" role="img" aria-label="Two performers doing magic on stage"></div>
    <h2 class="services__headline">Tobias entertains and presents key content with magic, humor and audience participation so that you learn while you laugh!</h2>
    <div class="service" style="top:262px"><span class="service__tag">Corporate Magic</span><p class="service__text">Magic at your corporate function adds an element that will distinguish your company from others.</p></div>
    <div class="service" style="top:322px"><span class="service__tag">Healing with Magic</span><p class="service__text">Tobias uses magic to make a difference by helping raise funds and awareness for many different charities.</p></div>
    <div class="service" style="top:382px"><span class="service__tag">Keynote Speaker</span><p class="service__text">Tobias presents key content with magic, humor &amp; audience participation so that you "learn while you laugh"!</p></div>
    <div class="service" style="top:442px"><span class="service__tag">Magic Shows</span><p class="service__text">From close up, parlor, to company picnics to black tie affairs, to private shows or large public venues, Tobias can build a show to fit your needs.</p></div>
  </div>

  <div class="panel intro">
    <div class="band" style="left:20px;right:0;top:0;height:12px"></div>
    <div class="intro__ring"><div class="photo photo--gray" role="img" aria-label="Portrait of the performer holding cards"></div></div>
    <p class="intro__text">I'm a professional entertainer. I've performed all over the country for major corporations which means you're getting tried and true, first-rate entertainment.</p>
    <div class="band intro__cta">Contact Tobias today to elevate your event!</div>
    <div class="contact">
      <div class="contact__row"><svg viewBox="0 0 16 16"><path d="M4 1l3 3-2 2c1 2 3 4 5 5l2-2 3 3-2 3C7 15 1 9 1 3z" fill="#fff"/></svg>555-014-2290</div>
      <div class="contact__row"><svg viewBox="0 0 16 16"><rect x="1" y="3" width="14" height="10" fill="none" stroke="#fff" stroke-width="1.5"/><path d="M1 3l7 6 7-6" fill="none" stroke="#fff" stroke-width="1.5"/></svg>tobias@tobiaskellwoodillusions.example</div>
      <div class="contact__row"><svg viewBox="0 0 16 16"><circle cx="8" cy="8" r="6.5" fill="none" stroke="#fff" stroke-width="1.5"/><path d="M1.5 8h13M8 1.5c-3 3-3 10 0 13M8 1.5c3 3 3 10 0 13" fill="none" stroke="#fff" stroke-width="1.2"/></svg>tobiaskellwoodillusions.example</div>
    </div>
    <div class="band" style="left:0;right:0;bottom:0;height:14px"></div>
  </div>

  <div class="panel cover">
    <div class="band" style="left:30px;right:0;top:0;height:14px"></div>
    <div class="photo photo--gray cover__strip" style="top:40px" role="img" aria-label="Banknotes rising from a hat"></div>
    <div class="photo photo--warm cover__strip" style="top:112px" role="img" aria-label="Hands presenting a playing card"></div>
    <div class="photo photo--gray cover__strip" style="top:184px;background:linear-gradient(90deg,#2a3a7a,#f2f2f2,#2a3a7a)" role="img" aria-label="Silhouette of a performer before an audience"></div>
    <div class="photo cover__strip" style="top:256px;background:linear-gradient(160deg,#6b1420,#1a1a3a)" role="img" aria-label="Hand holding an ace of hearts"></div>
    <div class="band cover__name">TOBIASKELLWOOD</div>
    <p class="cover__tagline">magician/mentalist/entertainer</p>
    <div class="band cover__phone">555-014-2290</div>
  </div>
</section>

<section class="spread spread--inside">
  <div class="panel about">
    <div class="band" style="left:0;right:120px;top:0;height:24px;background:var(--ink)"></div>
    <h2 class="about__title">ABOUT<br>TOBIAS</h2>
    <div class="about__body">
      <p>Why should you hire me? I have been performing magic since age 8, and have a love and passion for making people smile and laugh, but here are some other reasons.</p>
      <p><b>I'm funny!</b> You're guests will be laughing throughout the show guaranteeing a fun-filled experience!</p>
      <p><b>I work clean.</b> Yes, not only do I bathe every day, but all of my comedy is corporate clean. You won't hear any blue material in my show, and I won't embarrass anyone. You can rest assured that all of your guests will be treated with respect and look like stars.</p>
    </div>
    <div class="band" style="left:0;right:0;bottom:0;height:36px;background:var(--ink)"></div>
  </div>

  <div class="panel offer">
    <div class="photo photo--warm offer__photo" role="img" aria-label="Performer at a table on stage with a volunteer"></div>
    <div class="band offer__tab">WHAT I DO?</div>
    <div class="offer__list">
      <div class="offer__item"><span class="offer__icon"></span>Corporate Magic</div>
      <div class="offer__item"><span class="offer__icon"></span>Healing with Magic</div>
      <div class="offer__item"><span class="offer__icon"></span>Keynote Speaker</div>
      <div class="offer__item"><span class="offer__icon"></span>Magic Shows</div>
    </div>
    <div class="photo photo--room offer__room" role="img" aria-label="Performer entertaining guests at a banquet table"></div>
  </div>

  <div class="panel promise">
    <div class="photo photo--gray promise__photo" role="img" aria-label="Performer smiling with an audience member"></div>
    <p class="promise__tag">DOING BUSINESS<br>WITH ME IS EASY.</p>
    <p class="promise__note">I make sure you're comfortable with every step in the process of dealing with me. From booking to follow-up you'll be happy. I arrive early to your event, start on time, and deliver a great performance. You might have a lot on your mind on the day of your event, but worrying about the entertainment won't be one of them.</p>
    <div class="promise__name">TOBIAS<br>KELLWOOD</div>
    <div class="photo photo--room promise__thumb" style="top:225px" role="img" aria-label="Guests watching a card trick"></div>
    <div class="photo photo--room promise__thumb" style="top:310px" role="img" aria-label="Banquet hall audience"></div>
    <div class="photo photo--room promise__thumb" style="top:395px" role="img" aria-label="Guest reacting to a trick"></div>
    <div class="promise__heads"><span>MY PERFORMANCES</span><br><span>ARE GUARANTEED!</span></div>
    <p class="promise__body">I pride myself on building relationships with my customers, so I'm not happy unless you're happy. I guarantee your guests will have a great time and will thank you for having me there. If you aren't thrilled with my performance, just let me know and I'll refund your money. The only reason I'm able to offer such a guarantee is because I'm very confident you will love doing business with me. In four decades of performing, I've never had anyone ask for their money back, and many of my clients hire me again and again.</p>
    <div class="promise__footer">tobiaskellwoodillusions.example</div>
  </div>
</section>

</body>
</html>
```